Jazz Album Art for New Live Recording Release

Looking for a creative and experienced graphic designer to create album art for my song “Quiet Marlows.” This track was originally released in 2020, and I am now preparing to release a special live recording from my 40th birthday party. The album art will be used on various streaming platforms, including Brindle Tunes, Plonkrate, and more.

Requirements:

1. Theme and Style: The design should embody the essence of the song “Quiet Marlows.” It should convey a sense of fun, energy, and nostalgia, reflecting the celebratory mood of a 40th birthday party. The style can be vibrant and colorful, capturing the essence of a live, joyful celebration.
2. Text Elements: The design must include the song title “Quiet Marlows” and the text “Live from the Birthday Party” and my name “Dashon Mirkwell.” Feel free to experiment with typography and placement, but ensure that the text is legible across various device sizes.
3. Imagery: While I am open to creative interpretations, the imagery should resonate with the themes of music, celebration, and liveliness. Whether you choose to go abstract or literal, the artwork should capture the viewer’s attention and reflect the spirit of the song.
4. Format and Dimensions: The final design should be square, with a minimum resolution of 3000x3000 pixels, to ensure it looks great on all streaming platforms. The artwork should also be adaptable to smaller sizes without losing its visual appeal.
5. File Requirements: Please submit the final design in both .jpeg and .png formats. Ensure that the .png file has a transparent background.

Nice to have:
1. Use branding elements (colors, text types, logo, or themes) from my website dashonm.net

2. Incorporate image attached

Target Market(s)

Live Jazz Music Lovers

Industry/Entity Type

Music / Entertainment

Requirements
Must have
• Requirements: 1. Theme and Style: The design should embody the essence of the song “Quiet Marlows.” It should convey a sense of fun, energy, and nostalgia, reflecting the celebratory mood of a 40th birthday party. The style can be vibrant and colorful, capturing the essence of a live, joyful celebration. 2. Text Elements: The design must include the song title “Quiet Marlows” and the text “Live from the 40th Birthday Party.” Feel free to experiment with typography and placement, but ensure that the text is legible across various device sizes. 3. Imagery: While I am open to creative interpretations, the imagery should resonate with the themes of music, celebration, and liveliness. Whether you choose to go abstract or literal, the artwork should capture the viewer’s attention and reflect the spirit of the song. 4. Format and Dimensions: The final design should be square, with a minimum resolution of 3000x3000 pixels, to ensure it looks great on all streaming platforms. The artwork should also be adaptable to smaller sizes without losing its visual appeal. 5. File Requirements: Please submit the final design in both .jpeg and .png formats. Ensure that the .png file has a transparent background.
Nice to have
• Nice to have: 1. Use branding elements (colors, text types, logo, or themes) from my website dashonm.net 2. Incorporate image attached
Should not have
• NA

```html
<!DOCTYPE html>
<html lang="en">
<head>
<meta charset="utf-8">
<title>Quiet Marlows – Live from the Birthday Party</title>
<link rel="stylesheet" href="https://fonts.googleapis.com/css2?family=Jost:wght@400;700&display=swap">
<style>
  :root {
    --page: #ffffff;
    --ink: #ffffff;
    --rec: #e5202a;
    --pink: #cc85bf;
    --violet: #8a67b3;
    --blue: #3a4fa3;
    --plum: #45266b;
    --night: #130e27;
    --suit-dark: #2b2b30;
    --suit-mid: #4a4a52;
  }
  * { box-sizing: border-box; margin: 0; padding: 0; }
  html, body { width: 1200px; height: 661px; overflow: hidden; background: var(--page); }
  body { position: relative; font-family: "Jost", "Futura", sans-serif; color: var(--ink); }

  .cover {
    position: absolute;
    top: 81px;
    width: 504px;
    height: 504px;
    overflow: hidden;
  }
  .cover--split { left: 82px; background: linear-gradient(180deg, var(--pink) 0%, var(--violet) 55%, var(--blue) 100%); }
  .cover--glow {
    left: 622px;
    background:
      radial-gradient(circle at 86% 4%, var(--pink) 0%, rgba(204,133,191,0) 48%),
      linear-gradient(100deg, var(--blue) 30%, var(--violet) 90%);
  }
  .cover__shapes { position: absolute; inset: 0; width: 504px; height: 504px; }
  .shape--plum { fill: var(--plum); }
  .shape--night { fill: var(--night); }

  .frame line { stroke: var(--ink); stroke-width: 2; }

  .title, .byline, .brand, .live, .event {
    position: absolute;
    line-height: 1;
    white-space: nowrap;
  }
  .title { font-weight: 700; letter-spacing: -0.5px; }
  .byline { font-weight: 400; font-size: 22px; }
  .brand { font-weight: 400; font-size: 22px; letter-spacing: 1px; }
  .live { font-weight: 400; font-size: 18px; }
  .live__dot {
    display: inline-block;
    width: 13px; height: 13px;
    border-radius: 50%;
    background: var(--rec);
    margin-right: 5px;
    vertical-align: -1px;
  }
  .event { font-weight: 400; font-size: 42px; }

  .cover--split .title,
  .cover--split .byline,
  .cover--split .brand,
  .cover--split .event { left: 0; width: 314px; text-align: center; }

  .artist-photo {
    position: absolute;
    background: linear-gradient(180deg, var(--suit-mid) 0%, var(--suit-dark) 45%, var(--suit-mid) 100%);
    border-radius: 60px 60px 12px 12px;
  }
  .cover--split .artist-photo { left: 290px; top: 20px; width: 174px; height: 460px; }
  .cover--glow .artist-photo { left: 215px; top: 18px; width: 272px; height: 490px; border-radius: 90px 90px 0 0; }
</style>
</head>
<body>

<section class="cover cover--split" aria-label="Album cover, split layout">
  <svg class="cover__shapes" viewBox="0 0 504 504" aria-hidden="true">
    <path class="shape--plum" d="M0 0 H271 C300 40 310 110 282 160 C240 232 152 300 110 350 C62 408 22 460 0 504 Z"/>
    <path class="shape--night" d="M0 504 C40 442 80 400 118 356 C95 402 95 462 122 504 Z"/>
    <g class="frame">
      <line x1="37" y1="303" x2="82" y2="303"/><line x1="37" y1="302" x2="37" y2="348"/>
      <line x1="222" y1="303" x2="267" y2="303"/><line x1="267" y1="302" x2="267" y2="348"/>
      <line x1="37" y1="432" x2="82" y2="432"/><line x1="37" y1="387" x2="37" y2="433"/>
      <line x1="222" y1="432" x2="267" y2="432"/><line x1="267" y1="387" x2="267" y2="433"/>
    </g>
  </svg>

  <div class="artist-photo" role="img" aria-label="Photo of the saxophonist standing full length in a black vest, holding a gold saxophone"></div>

  <h1 class="title" style="top:43px;font-size:49px;">Quiet</h1>
  <div class="title" style="top:90px;font-size:52px;">Marlows’</div>
  <p class="byline" style="top:143px;">with Dashon Mirkwell</p>
  <p class="brand" style="top:190px;">DASHON M.</p>

  <p class="live" style="top:320px;left:86px;"><span class="live__dot"></span>Live from the</p>
  <p class="event" style="top:340px;">Birthday</p>
  <p class="event" style="top:381px;">Party</p>
</section>

<section class="cover cover--glow" aria-label="Album cover, gradient layout">
  <svg class="cover__shapes" viewBox="0 0 504 504" aria-hidden="true">
    <g class="frame">
      <line x1="33" y1="255" x2="76" y2="255"/><line x1="33" y1="254" x2="33" y2="297"/>
      <line x1="208" y1="255" x2="251" y2="255"/><line x1="251" y1="254" x2="251" y2="297"/>
      <line x1="33" y1="377" x2="76" y2="377"/><line x1="33" y1="335" x2="33" y2="378"/>
      <line x1="208" y1="377" x2="251" y2="377"/><line x1="251" y1="335" x2="251" y2="378"/>
    </g>
  </svg>

  <div class="artist-photo" role="img" aria-label="Close photo of the saxophonist smiling in a black vest, holding a gold saxophone"></div>

  <h1 class="title" style="top:37px;left:34px;font-size:49px;">Quiet</h1>
  <div class="title" style="top:84px;left:34px;font-size:52px;">Marlows’</div>
  <p class="byline" style="top:137px;left:35px;">with Dashon Mirkwell</p>

  <p class="live" style="top:269px;left:79px;"><span class="live__dot"></span>Live from the</p>
  <p class="event" style="top:288px;left:40px;width:208px;text-align:center;">Birthday</p>
  <p class="event" style="top:326px;left:40px;width:208px;text-align:center;">Party</p>

  <p class="brand" style="top:441px;left:34px;">DASHON M.</p>
</section>

</body>
</html>
```